Web Design Project

Dear designer(s),

I need a design for a shop who's specialized into...

-Material to fix or do tailor made clothing (cloth, buttons, zippers etc)
-Curtains (static/pull-up)
-Blinds (plastic/wood)

that kind of stuff.

Good thing is that I can provide a lot of pretty photo's to work with. I have 3.5 Gigabyte of 300-1200 dpi photo's altho I converted most of them to 72dpi for your convenience (75Mb).

You can download the working material from this quellbin link:

http://files.quellbin.net/u/31920586/Velunor.zip

this is an updated file, it contains the dutch menu items to use in your design

http://files.quellbin.net/u/31920586/Velunor_Content.txt

Notice: take your time to come up with something nice. I prefer 1 or 2 designs from a designer that has been thinked of, than 5 quick ones.
Updates

Thank you for those who posted designs already but I want to clarify something.

As I mentioned it's a shop, that's a physical shop and not a webshop.

So you can safe some time and skip drawing the shopping cart icons, shop items on the homepage and other shop related things.

They don't want to start online reselling as they already spend most of their time in their shop to catch up with all orders.

Keep up the good work!

Industry/Entity Type

Clothing

Requirements
Nice to have
• Maybe the hi-res pictures can be used as background ratotor that appears left/right next to the centered website content?

Since there is a lot of material each section might have his topic linked set of thumbnails that opens a bigger image on clicking?

```html
<!DOCTYPE html>
<html lang="en">
<head>
<meta charset="utf-8">
<title>Velunor – Stoffen, Tafellinnen, Raambekleding</title>
<link href="https://fonts.googleapis.com/css2?family=Arimo:wght@400&display=swap" rel="stylesheet">
<style>
:root{
  --bar:#dcdcdd;
  --bar-line:#ffffff;
  --text:#555555;
  --muted:#6a6a6a;
  --heading:#1f4e79;
  --brand:#1e6fc2;
  --rule:#cfcfcf;
  --frame:#e2e2e2;
  --bg:#ffffff;
}
*{margin:0;padding:0;box-sizing:border-box}
html,body{width:975px;height:1200px;overflow:hidden;background:var(--bg)}
body{font-family:"Arimo",Arial,sans-serif;color:var(--text);position:relative}
.page{position:absolute;left:38px;top:0;width:899px;height:1200px}

.main-nav{position:absolute;top:10px;left:0;width:899px;height:28px;display:flex;background:var(--bar)}
.main-nav a{height:28px;line-height:28px;text-align:center;font-size:14px;color:#555;text-decoration:none;border-right:1px solid var(--bar-line)}
.main-nav a:last-child{border-right:none}

.brand{position:absolute;top:55px;left:258px;width:383px;height:104px;border:1px solid #ececec;display:flex;align-items:center;justify-content:space-between;padding:0 10px 0 10px}
.brand-name{font-size:38px;color:var(--brand);letter-spacing:-0.5px}
.brand-side{display:flex;flex-direction:column;align-items:flex-start;font-size:14px;color:#7a7a7a;line-height:17px}
.brand-side .web{font-size:22px;margin-top:10px;line-height:24px}
.contact-line{position:absolute;top:172px;left:0;width:899px;text-align:center;font-size:10px;color:var(--muted)}

.hero{position:absolute;top:203px;left:0;width:899px;height:439px;background:linear-gradient(180deg,#8e9aa8 0%,#b7bec6 28%,#6c5a48 40%,#d9d9d6 55%,#8d8b88 75%,#a6a3a0 100%)}

.col{position:absolute;top:676px;width:287px}
.col-1{left:0}.col-2{left:306px}.col-3{left:612px}
.col-title{height:28px;line-height:28px;background:var(--bar);font-size:14px;color:#555;padding-left:22px}
.col-1 .col-title{padding-left:22px}
.col-2 .col-title,.col-3 .col-title{padding-left:20px}

.photo-frame{border:1px solid var(--frame);padding:9px;background:#fff}
.feature{margin-top:27px;width:287px;height:160px}
.feature .photo{width:267px;height:140px;background:linear-gradient(135deg,#eef0f1 0%,#cfd3d6 45%,#2f3338 60%,#e8e9ea 80%)}

h3.lead{font-weight:400;color:var(--heading);font-size:15px;line-height:21px}
p.body{font-size:12px;line-height:17.2px;color:var(--text)}
.col-1 h3.lead{margin:26px 0 0 2px}
.col-1 p.body{margin:19px 0 0 3px}
.col-2 h3.lead{margin:26px 0 0 2px}
.col-2 p.body{margin:19px 0 0 2px}
.col-2 p.body + p.body{margin-top:17px}

.teaser{display:flex;height:114px;border-bottom:1px solid #e4e4e4}
.teaser:first-of-type{margin-top:19px}
.teaser + .teaser{padding-top:9px;height:114px}
.teaser:last-child{border-bottom:none}
.teaser .photo-frame{width:105px;height:96px;flex:none}
.teaser .photo{width:85px;height:76px}
.t1{background:linear-gradient(135deg,#5a4437,#c9c4be 55%,#3b3331)}
.t2{background:linear-gradient(135deg,#d8d6cf,#f2f1ee 50%,#8a8780)}
.t3{background:linear-gradient(135deg,#9a7e62,#efefee 50%,#cfcac3)}
.teaser-text{margin-left:16px;padding-top:4px}
.teaser-text h4{font-weight:400;font-size:15.5px;line-height:20px;color:var(--heading);text-transform:uppercase}
.teaser-text p{font-size:12px;line-height:17px;margin-top:8px;color:var(--text)}

.footer{position:absolute;top:1122px;left:0;width:899px;border-top:1px solid var(--rule);text-align:center;font-size:10px;color:var(--muted);padding-top:9px}
</style>
</head>
<body>
<div class="page">
  <nav class="main-nav">
    <a href="#" style="width:117px">Home</a>
    <a href="#" style="width:156px">Cloth - Fabric</a>
    <a href="#" style="width:142px">Table cloth</a>
    <a href="#" style="width:189px">Decoration cloth</a>
    <a href="#" style="width:163px">Pull systems</a>
    <a href="#" style="width:132px">Contact</a>
  </nav>

  <header class="brand">
    <span class="brand-name">velunor</span>
    <div class="brand-side">
      <span>Stoffen</span>
      <span>Tafellinnen</span>
      <span>Raambekleding</span>
      <span class="web">www.velunor.be</span>
    </div>
  </header>
  <p class="contact-line">Lindenweg 14 &nbsp;|&nbsp; B-9000 Aldenhem &nbsp;|&nbsp; T: 051/38.27.64 &nbsp;|&nbsp; F: 051/38.22.90 &nbsp;|&nbsp; Email: info@velunor.be</p>

  <div class="hero" role="img" aria-label="Photograph of white woven table linen draped over a driftwood bench with glass bottles and a jug, on a pebble beach by the sea"></div>

  <section class="col col-1">
    <h2 class="col-title">Cloth - Fabric</h2>
    <div class="photo-frame feature">
      <div class="photo" role="img" aria-label="Bright interior with black leather chairs and a white low table"></div>
    </div>
    <h3 class="lead">Lorem ipsum dolor sit amet, eam</h3>
    <p class="body">Lorem ipsum dolor sit amet, eam nusquam similique sadipscing eu, ius mutat periculis disputationi ea, id cum sale persecuti. Vide imperdiet ea mei, sed dictas appetere oporteat ne. Ignota inimicus recteque est te, paulo graeci ornatus sit ea. Usu dicta senserit dissentiunt eu,</p>
  </section>

  <section class="col col-2">
    <h2 class="col-title">Table cloth</h2>
    <h3 class="lead">Lorem ipsum dolor sit amet, eam nusquam similique sadipscing eu, ius mutat periculis disputationi ea, id cum</h3>
    <p class="body">Lorem ipsum dolor sit amet, eam nusquam similique sadipscing eu, ius mutat periculis disputationi ea, id cum sale persecuti. Vide imperdiet ea mei, sed dictas appetere oporteat ne. Ignota inimicus recteque est te, paulo graeci</p>
    <p class="body">Lorem ipsum dolor sit amet, eam nusquam similique sadipscing eu, ius mutat periculis disputationi ea, id cum sale persecuti. Vide imperdiet ea mei, sed dictas appetere oporteat ne. Ignota inimicus recteque est te, paulo graeci ornatus sit ea. Usu dicta senserit dissentiunt eu, graecis incorrupte usu id, ei laoreet principes nam.</p>
  </section>

  <section class="col col-3">
    <h2 class="col-title">Decoration cloth</h2>
    <div class="teaser">
      <div class="photo-frame"><div class="photo t1" role="img" aria-label="Dining room with dark wooden blinds"></div></div>
      <div class="teaser-text"><h4>Vide imperdiet laboris</h4><p>Lorem ipsum dolor sit amet, eam nusquam similique</p></div>
    </div>
    <div class="teaser">
      <div class="photo-frame"><div class="photo t2" role="img" aria-label="Kitchen with light roller blinds and pendant lamps"></div></div>
      <div class="teaser-text"><h4>Vide imperdiet laboris</h4><p>Lorem ipsum dolor sit amet, eam nusquam similique</p></div>
    </div>
    <div class="teaser">
      <div class="photo-frame"><div class="photo t3" role="img" aria-label="Living room with wooden venetian blinds and a white sofa"></div></div>
      <div class="teaser-text"><h4>Vide imperdiet laboris</h4><p>Lorem ipsum dolor sit amet, eam nusquam similique</p></div>
    </div>
  </section>

  <footer class="footer">Velunor &nbsp;|&nbsp; Lindenweg 14 &nbsp;|&nbsp; B-9000 Aldenhem &nbsp;|&nbsp; T: 051/38.27.64 &nbsp;|&nbsp; F: 051/38.22.90 &nbsp;|&nbsp; Email: info@velunor.be</footer>
</div>
</body>
</html>
```